Business Card Design

Business Card for professional consulting firm working with large financial institutions.

Target Market(s)

Executive buyers

Industry/Entity Type

Banking

Contact Information for Business Card

Mild creativity wanted. Not boring, but do elaborate artwork.

Font styles to use
Serif
Sans Serif

Colors

Designer to choose colors to be used in the design.

Requirements
Must have
• Standard business card features - company name, individual name, telephone, website, email, locations.
Nice to have
• Two colors
Should not have
• too many colors, fancy printing, cartoons.

```html
<!DOCTYPE html>
<html lang="en">
<head>
<meta charset="utf-8">
<title>k7advisory – Business Card</title>
<link href="https://fonts.googleapis.com/css2?family=Tinos:wght@400;700&display=swap" rel="stylesheet">
<style>
  :root {
    --stage: #2b2623;
    --card-black: #0b0b0b;
    --card-black-hi: #2a2a2a;
    --card-white: #f6f6f6;
    --swoosh-grey: #b9b9b9;
    --text-light: #e8e8e8;
    --text-muted: #c9c9c9;
    --ink: #1a1a1a;
  }
  * { margin: 0; padding: 0; box-sizing: border-box; }
  html, body { width: 1200px; height: 886px; overflow: hidden; }
  body {
    background: var(--stage);
    font-family: "Tinos", "Times New Roman", serif;
    position: relative;
  }
  .card {
    position: absolute;
    width: 560px;
    height: 320px;
    border-radius: 18px;
    overflow: hidden;
    left: 320px;
    box-shadow: 0 12px 30px rgba(0,0,0,.45);
  }
  .card--back { top: 80px; }
  .card--front { top: 486px; }
  .card svg.card-art { position: absolute; inset: 0; }

  .brand {
    position: absolute;
    display: flex;
    align-items: center;
    gap: 8px;
    font-weight: 400;
    letter-spacing: .5px;
  }
  .brand-dot { width: 8px; height: 8px; border-radius: 50%; }
  .card--back .brand {
    left: 0; right: 0; top: 0; bottom: 0;
    justify-content: center;
    color: var(--text-light);
    font-size: 40px;
  }
  .card--back .brand-dot { background: var(--text-light); }
  .card--front .brand {
    left: 120px; top: 58px;
    color: var(--ink);
    font-size: 30px;
  }
  .card--front .brand-dot { background: var(--ink); }

  .contact {
    position: absolute;
    right: 28px;
    bottom: 22px;
    text-align: right;
    color: var(--text-muted);
    font-size: 14px;
    line-height: 1.25;
  }
  .contact .person-name { color: var(--text-light); font-size: 23px; font-weight: 700; line-height: 1.1; }
  .contact .person-title { font-size: 16px; margin-bottom: 6px; }
  .contact .address { margin-bottom: 6px; }
  .contact .line { display: flex; justify-content: flex-end; align-items: center; gap: 8px; }
  .contact .line svg { width: 13px; height: 13px; fill: var(--text-light); flex: none; }
</style>
</head>
<body>

<section class="card card--back" aria-label="Card back">
  <svg class="card-art" viewBox="0 0 560 320" aria-hidden="true">
    <defs>
      <linearGradient id="backGloss" x1="0" y1="0" x2="1" y2="0">
        <stop offset="0" stop-color="#0b0b0b"/>
        <stop offset=".55" stop-color="#0b0b0b"/>
        <stop offset=".7" stop-color="#2a2a2a"/>
        <stop offset=".85" stop-color="#0b0b0b"/>
      </linearGradient>
    </defs>
    <rect width="560" height="320" fill="url(#backGloss)"/>
  </svg>
  <div class="brand"><span class="brand-name">k7advisory</span><span class="brand-dot"></span></div>
</section>

<section class="card card--front" aria-label="Card front">
  <svg class="card-art" viewBox="0 0 560 320" aria-hidden="true">
    <rect width="560" height="320" fill="var(--card-black)"/>
    <path d="M0,0 H500 C525,5 520,40 490,80 C420,180 240,270 20,300 L0,302 Z" fill="var(--swoosh-grey)"/>
    <path d="M0,0 H490 C512,4 505,36 478,74 C410,170 235,258 14,288 L0,290 Z" fill="var(--card-white)"/>
  </svg>
  <div class="brand"><span class="brand-name">k7advisory</span><span class="brand-dot"></span></div>
  <div class="contact">
    <div class="person-name">Daniel Reyes</div>
    <div class="person-title">Managing Director</div>
    <div class="address">4120 Harbor View Road<br>Juneau, Alaska 99801</div>
    <div class="line">555 210 4786
      <svg viewBox="0 0 24 24"><path d="M6.6 10.8a15.1 15.1 0 0 0 6.6 6.6l2.2-2.2a1 1 0 0 1 1-.25 11.4 11.4 0 0 0 3.6.6 1 1 0 0 1 1 1V20a1 1 0 0 1-1 1A17 17 0 0 1 3 4a1 1 0 0 1 1-1h3.5a1 1 0 0 1 1 1c0 1.25.2 2.45.6 3.6a1 1 0 0 1-.25 1z"/></svg>
    </div>
    <div class="line">info@k7advisory.com
      <svg viewBox="0 0 24 24"><path d="M2 5h20v14H2z M3 6l9 7 9-7" fill="none" stroke="currentColor"/><path d="M2 5h20v14H2zM4 7v10h16V7l-8 6z"/></svg>
    </div>
    <div class="line">www.k7advisory.com
      <svg viewBox="0 0 24 24"><circle cx="12" cy="12" r="10"/></svg>
    </div>
  </div>
</section>

</body>
</html>
```